Business card design only (Have Logo Online) Shoudl be quick and easy for designer

We would like to have a business card design that is in-line with our company logo. Final deliverables should include two EPS extension file. One for the front card design and the other the back-end design. Please also indicate the font style used.

Advisory Pebbles is a social enterprise that focuses on utilizing technology, unique methodologies and international partnerships to provide a one-stop location for economical and dependable IT-related solutions.

Target Market(s)

Micro, small and medium business owners.

Industry/Entity Type

Business

Requirements
Must have
• The business card should incorporate our company logo.
Nice to have
• A little web 2.0 style would be nice but I haven''t decided yet.

```html
<!DOCTYPE html>
<html lang="en">
<head>
<meta charset="utf-8">
<title>Advisory Pebbles – Business Card</title>
<link href="https://fonts.googleapis.com/css2?family=Encode+Sans:wght@400;700&display=swap" rel="stylesheet">
<style>
  :root {
    --page: #ffffff;
    --brand-green: #5a9260;
    --brand-green-dark: #4c8453;
    --leaf-light: #b8da98;
    --mist: #e3f1e4;
    --ink: #111111;
    --paper: #ffffff;
  }
  * { box-sizing: border-box; margin: 0; padding: 0; }
  html, body {
    width: 1112px;
    height: 1200px;
    overflow: hidden;
    background: var(--page);
    font-family: "Encode Sans", Arial, sans-serif;
  }
  .canvas { position: relative; width: 1112px; height: 1200px; }

  .card { position: absolute; left: 68px; width: 968px; }

  /* Front face */
  .card-front {
    top: 68px;
    height: 470px;
    background: var(--brand-green);
  }
  .front-brand {
    position: absolute;
    left: 0; right: 0; top: 200px;
    display: flex;
    align-items: center;
    justify-content: center;
    gap: 20px;
  }
  .front-brand .brand-dot {
    width: 58px; height: 58px;
    border-radius: 50%;
    background: var(--paper);
  }
  .front-brand .brand-name {
    color: var(--paper);
    font-weight: 700;
    font-size: 56px;
    letter-spacing: 1px;
  }

  /* Back face */
  .card-back {
    top: 650px;
    height: 471px;
    background: var(--paper);
    border: 1px solid var(--brand-green);
    overflow: hidden;
  }
  .back-pattern {
    position: absolute;
    left: 330px; top: 0; right: 0; bottom: 0;
    background: linear-gradient(100deg, rgba(227,241,228,0) 0%, var(--mist) 45%, var(--mist) 100%);
  }
  .back-brand {
    position: absolute;
    left: 80px; top: 120px;
    display: flex;
    align-items: center;
    gap: 14px;
  }
  .back-brand .brand-dot {
    width: 44px; height: 44px;
    border-radius: 50%;
    background: var(--leaf-light);
  }
  .back-brand .brand-name {
    color: var(--brand-green-dark);
    font-weight: 700;
    font-size: 34px;
    letter-spacing: 0.5px;
  }
  .holder {
    position: absolute;
    left: 82px; top: 290px;
    color: var(--ink);
    font-size: 33px;
    line-height: 41px;
  }
  .holder-name { font-weight: 700; }
  .holder-role { font-weight: 400; }

  .contact {
    position: absolute;
    left: 450px; top: 296px;
    list-style: none;
    color: var(--ink);
    font-size: 22px;
    line-height: 34.5px;
  }
</style>
</head>
<body>
<main class="canvas">
  <section class="card card-front" aria-label="Card front">
    <div class="front-brand">
      <span class="brand-dot"></span>
      <span class="brand-name">Advisory Pebbles</span>
    </div>
  </section>

  <section class="card card-back" aria-label="Card back">
    <div class="back-pattern" role="img" aria-label="Faint repeated brand emblem pattern in pale green"></div>
    <div class="back-brand">
      <span class="brand-dot"></span>
      <span class="brand-name">Advisory Pebbles</span>
    </div>
    <div class="holder">
      <p class="holder-name">Marlo Vance</p>
      <p class="holder-role">Founder</p>
    </div>
    <ul class="contact">
      <li>marlo.vance@advisorypebbles.com</li>
      <li>4120 Alder Row, BC Canada V6K 2J3</li>
      <li>1-604-555-0148</li>
      <li>www.advisorypebbles.com</li>
    </ul>
  </section>
</main>
</body>
</html>
```